Velvet Facet - High end custom Jewelry website

I need a web design for an online custom jewelry company called Velvet Facet. (www.velvetfacetgems.com) this company specializes in high-end custom made engagement rings, wedding bands and jewelry of all kinds (necklaces, earrings, bracelets etc)All our jewelry uses diamonds so there must be a focus on diamonds on every type of jewelry we will be designing off the website.

We are a company located in New York City but our website will
aim to cater to international, national clients and as well as New York city residents.The company low overhead provides diamonds and precious metal at a discounted costs compared to its competitors. Velvet Facet makes unique custom diamond jewelry of a higher quality and at a lower price than carriage trade retail jewellers. (meaning that our company allows our customers to save money on diamond jewelry then they would if they bought from any known store or company)

The website will act as a tool for our customers to create their own jewelry. The way they will do this is by uploading pictures of what they like, they can post any pictures they want (from drawings, to actual copy and pasted pictures from other websites of designs) From these designs we will create a 3D digital image of the jewelry they like and customize it - however they want (colours, size etc) and then give them a quote in price. From the quote they will either approve it and we can have it made for them in 1 weeks time. If they decline it we will try to do whatever it is they want for the design to suit their needs.

We want the website to be simple and user friendly since people will be working on it to create their own individual jewelry pieces. Therefore some useful headings should include:

"Custom Jewellery" or something like "your design" "Custom Design"

a drop heading here should show the following steps into creating the jewelry.

step 1:
upload pictures of the designs you like
step 2:
What is your ring size?
Step 3:
What setting would you like your ring in? platinum, 14k etc..
Step 4:
What is your budget?
Step 5 :
Once you’ve uploaded pictures and give an explanation of what you want then we will contact you by phone or email and proceed to design your ring. Give us your contact info in this step.

Other then that other headings id like to see on the site are:

"Home"
main page with appealing picture which I can later add text to it explaining our company

"About us"
will include a brief section of who we are

"Wedding/engagment"

We are based in New York City and our company offers a one-to-one personal service to our clients ensuring their expectations are well met and, if we can help it, surpassed. We are a personal shopping and diamond supplier to individuals. Custom design is our speciality weather it be wedding ring, engagement ring or anniversary ring we aim to create distinctive designs that both reflect your personality as well as the beauty of the gemstones used in your piece. We use platinum, 14l-18k gold and diamonds to whatever it is that you may desire.
We in our company believe that we are privileged to be a part of one of the biggest events in our customer’s lives, and we pride ourselves on making sure that our customers have the best experience possible. As the diamond is the center piece of every engagement ring, we at VF make sure that our clients find the best diamond possible that is within their budget. Similarly, we work with established jewellery artisans from Belgium to provide the highest possible craftsmanship to a ring design of your choice. We make sure that our rings are made by the true and tried traditional methods focused on quality rather than quantity and of course our diamonds are QLB certified.

Diamonds

A section that explains where our diamonds come from. A heading will drop down here that is a diamond guide, as shown below.
Diamond Guide

An overview of the 4 C’s and different settings, a section for a brief education on diamonds.
Client Experiences

A section where clients share their experiences with Velvet Facet and can post pictures and share stories about their engagement etc.

The colour i would like to see are white and black, white and dark blue or royal blue. I don't think pastel colours will look good with this, maybe accents of purple or something pastel but for the main colours I want to keep it classic and sophisticated since it is a diamond company.

"Sign in | Check out"
where users are able to create a profile and upload their pictures and create their designs..

and a "search section"

or something along these lines or if you can incorporate both:

Exquisite craftsmanship Finest quality diamonds
Will beat any competitors price by twenty to seventy percent guaranteed
Price quotes whitin24 hours

Upload design picture or sketch
Receive price quote within 24hours
Receive and approve free customized design
Receive you jewelry in 1 week or less

Engagment Ring or necklace, earring, etc
Name
EMail
phone
Competitior Link
Budget

The final design should communicate that Velvet Facet is a custom jewelry site that allows individuals to personalize any type of jewellery they want with diamonds - at a fraction of the cost in comparison to any other out there. Our team works very hard to ensure that you will be so involved in the custom order process that there is no chance of something not being made to your requests. Jewelry is made to the highest standard or it does not ship in the first place. In the event a custom order does not suit a customer, we will take returns within 14 days of delivery less a 25% restocking fee.

Target Market(s)

middle class and upper class people ages 25-45

Industry/Entity Type

Digital

Requirements
Must have
• We have the logo now that I will attach BUT if you want to design something else please feel free ! I am open to all designs and ideas.
My logo now is simply a sketch so even if we make it look a bit more professional and classy I would like that, I think I want to keep it simple just black and white and maybe make the diamond shiny if possible. other then black in white I liked the gold and black combination too.. but as I said open to any other creative ideas!

can take pictures of jewelry off this website:
http://www.brimwelldrafthouse.com/library/rings.html
Nice to have
• We already have a logo but we would like to see a banner or something that indicated saving money on diamond jewelry without it looking tacky or too cheap..

Also would like to see artistic pictures if you can of jewelry alongside very simple designs of jewelry that the masses like, (anything trendy or appealing to the eye)

cursive or elegant writing could be nice, flash could also be incorporated in the main page..

Should not have
• Nothing to old fashioned, when I mean elegant maybe just the the name of the company in cursive writing (Velvet Facet) but the actual headings and font on the website to be in a widely used font on jewelry websites. Please no hot pink colours or anything neon..
no times new roman font..

```html
<!DOCTYPE html>
<html lang="en">
<head>
<meta charset="utf-8">
<title>Velvet Facet – Custom Diamond Jewellery</title>
<link rel="stylesheet" href="https://fonts.googleapis.com/css2?family=PT+Sans:wght@400;700&family=PT+Sans+Narrow:wght@400;700&display=swap">
<style>
  :root{
    --cream:#efe6cf;
    --cream-light:#f6f0e0;
    --navy:#0f2a66;
    --navy-deep:#0a1d4a;
    --royal:#2a4e9a;
    --ink:#1d1d1d;
    --grey:#555;
    --line:#cfd3da;
    --sky:#b5dcf2;
    --page:#f3f4f6;
    --white:#fff;
  }
  *{box-sizing:border-box;margin:0;padding:0}
  html,body{width:935px;height:1200px;overflow:hidden}
  body{position:relative;background:var(--page);font-family:"PT Sans",sans-serif;color:var(--ink)}
  .abs{position:absolute}
  .narrow{font-family:"PT Sans Narrow",sans-serif}

  /* header */
  .site-header{left:0;top:0;width:935px;height:126px;background:linear-gradient(180deg,var(--cream-light),var(--cream))}
  .brand{left:134px;top:0;width:164px;height:124px;background:#f7f0dc;border:1px solid #e2d6b8;display:flex;flex-direction:column;align-items:center;justify-content:center;gap:10px}
  .brand-dot{width:14px;height:14px;border-radius:50%;background:var(--ink)}
  .brand-name{font-size:13px;letter-spacing:2px;color:var(--ink);font-weight:700}
  .cart{left:544px;top:22px;font-size:9.5px;color:#333;display:flex;align-items:center;gap:5px}
  .search{left:624px;top:16px;width:152px;height:26px;background:var(--white);border:1px solid #ccc;font-size:9.5px;font-style:italic;color:#666;padding:7px 17px}
  .search-btn{left:776px;top:16px;width:32px;height:26px;background:var(--navy);display:flex;align-items:center;justify-content:center}
  .custom-cta{left:626px;top:62px;width:178px;height:53px;background:linear-gradient(#fff,#eceef2);border:1px solid #d8d8d8;border-radius:5px;box-shadow:0 1px 3px rgba(0,0,0,.2);padding:7px 14px}
  .custom-cta b{display:block;color:var(--royal);font-size:15px;font-weight:700}
  .custom-cta span{display:block;color:#444;font-size:12.5px}

  /* nav */
  .main-nav{left:0;top:126px;width:935px;height:34px;background:linear-gradient(180deg,#1d3f7e,var(--navy-deep));display:flex;padding-left:133px}
  .main-nav a{color:var(--white);text-decoration:none;font-size:12px;height:34px;display:flex;align-items:center;justify-content:center;border-right:1px solid rgba(255,255,255,.15)}
  .main-nav a.active{background:linear-gradient(180deg,#3b63b5,#1f438d)}

  /* hero */
  .hero{left:0;top:160px;width:935px;height:334px;background:linear-gradient(180deg,#05070f 0%,#0b1227 60%,#1e2a4e 100%);box-shadow:0 3px 4px rgba(0,0,0,.3)}
  .hero-photo{left:308px;top:160px;width:568px;height:334px;background:radial-gradient(ellipse at 60% 95%,#c9ccd6 0%,#6b7390 30%,rgba(20,26,50,0) 70%),radial-gradient(ellipse at 55% 35%,#3a3f52 0%,rgba(0,0,0,0) 60%)}
  .hero-title{left:138px;top:222px;color:#f2ebd6;font-size:15px}
  .hero-lead{left:140px;top:258px;color:#e6e6e6;font-size:10.5px}
  .hero-copy{left:140px;top:286px;width:265px;color:#dcdcdc;font-size:9px;line-height:14px;text-align:justify}
  .hero-btn{left:140px;top:372px;width:111px;height:27px;background:#1b2d5e;border-radius:3px;color:var(--white);font-size:11px;font-weight:700;display:flex;align-items:center;justify-content:center}
  .slide-arrow{top:288px;width:28px;height:28px;border-radius:50%;background:#d9dadd;display:flex;align-items:center;justify-content:center}

  /* categories */
  .category{top:521px;width:208px;height:147px;border-radius:6px;overflow:hidden;background:#000;box-shadow:0 4px 4px -2px rgba(0,0,0,.3)}
  .category-head{height:32px;background:linear-gradient(180deg,#2c4f9c,#1c3a80);color:var(--white);font-size:18px;padding:5px 22px}
  .category-photo{height:115px}
  .view-more{right:0;bottom:0;width:77px;height:24px;background:var(--navy);color:var(--white);font-size:9.5px;font-weight:700;display:flex;align-items:center;justify-content:center;border-top-left-radius:6px}

  /* enquiry form */
  .enquiry{left:137px;top:696px;width:200px;height:250px;background:var(--white);border:1px solid #e4e6ea;border-radius:5px}
  .enquiry h2{position:absolute;left:57px;top:10px;font-size:15px;font-weight:400;color:#222}
  .ring-icon{left:0;top:-12px;width:42px;height:46px;border-radius:50%;background:radial-gradient(circle,#fff 35%,#c7ccd4 40%,#eef0f3 55%,rgba(255,255,255,0) 60%)}
  .field{left:14px;width:172px;height:24px;border:1px solid #c8c8c8;border-radius:2px;box-shadow:inset 0 1px 2px rgba(0,0,0,.1);font-size:8.5px;font-style:italic;color:#777;padding:6px 12px}
  .submit{left:122px;top:214px;width:63px;height:21px;background:var(--navy);border-radius:11px;color:var(--white);font-size:11.5px;font-style:italic;font-weight:700;display:flex;align-items:center;justify-content:center}
  .offer{left:137px;top:964px;width:199px;height:90px;background:var(--navy);border-radius:3px}
  .offer-photo{left:12px;top:4px;width:72px;height:82px;border-radius:40%;background:radial-gradient(circle,#3150a0 30%,#b8bec9 36%,#e5e8ee 48%,rgba(15,42,102,0) 60%)}
  .offer b{left:96px;top:26px;color:#f0e6c4;font-size:17px}
  .offer span{left:96px;top:55px;color:var(--white);font-size:13px;font-weight:700}

  /* products */
  .products-title{left:367px;top:699px;color:var(--navy);font-size:19px;font-weight:700}
  .pager{top:714px;width:9px;height:9px;background:var(--royal);border-radius:2px;display:flex;align-items:center;justify-content:center}
  .product{width:219px;height:135px;background:var(--sky)}
  .product-photo{left:6px;top:22px;width:98px;height:98px;border-radius:50%;background:radial-gradient(circle,#b5dcf2 40%,#d8dce2 46%,#f2f4f7 56%,rgba(181,220,242,0) 64%)}
  .product h3{position:absolute;left:107px;top:12px;font-family:"PT Sans Narrow",sans-serif;font-size:13.5px;font-weight:700}
  .product p{position:absolute;left:110px;top:34px;width:102px;font-size:8px;line-height:12.4px;color:#222}
  .details{left:114px;top:101px;width:63px;height:25px;background:linear-gradient(#333,#000);border-radius:3px;color:var(--white);font-size:10.5px;font-weight:700;display:flex;align-items:center;justify-content:center}

  /* footer */
  .site-footer{left:0;top:1070px;width:935px;height:130px;background:#f1f2f4;border-top:1px solid #e1e3e7}
  .footer-lines{left:139px;top:1092px;font-size:9.5px;color:#555;line-height:19px}
  .social{top:1089px;width:16px;height:16px;border-radius:2px}
  .copyright{left:600px;top:1130px;width:209px;text-align:right;font-size:8.5px;color:#444}
</style>
</head>
<body>

<header class="abs site-header" aria-label="Header"></header>
<div class="abs brand"><span class="brand-dot"></span><span class="brand-name">VELVET FACET</span></div>
<div class="abs cart">
  <svg width="11" height="10" viewBox="0 0 11 10"><path d="M0 1h2l1.5 5h6l1-3.5H3" fill="none" stroke="#444" stroke-width="1"/><circle cx="4" cy="8.5" r="1" fill="#444"/><circle cx="9" cy="8.5" r="1" fill="#444"/></svg>
  Cart (0) items
</div>
<div class="abs search">Search</div>
<div class="abs search-btn"><svg width="14" height="14" viewBox="0 0 14 14"><circle cx="6" cy="6" r="4.2" fill="none" stroke="#fff" stroke-width="2"/><path d="M9 9l3.5 3.5" stroke="#fff" stroke-width="2.2" stroke-linecap="round"/></svg></div>
<div class="abs custom-cta"><b>Custom Jewellery</b><span>Create your own jewellery</span></div>

<nav class="abs main-nav">
  <a class="active" href="#" style="width:74px">Home</a>
  <a href="#" style="width:110px">About Us</a>
  <a href="#" style="width:105px">Products</a>
  <a href="#" style="width:99px">Services</a>
  <a href="#" style="width:125px">Testimonials</a>
  <a href="#" style="width:110px;border-right:0">Contact Us</a>
</nav>

<section class="abs hero"></section>
<div class="abs hero-photo" role="img" aria-label="Four diamond engagement rings reflected on a dark glossy surface"></div>
<h1 class="abs hero-title" style="font-weight:400">We Do Custom Made Necklaces, Earrings, Bracelet</h1>
<p class="abs hero-lead">Sed ut perspiciatis unde omnis iste natus error.</p>
<p class="abs hero-copy">Sit voluptatem accusantium doloremque laudantium, totam rem aperiam.Sed ut perspiciatis unde omnis iste natus error sit voluptatem accusantium doloremque laudantium, totam rem aperiam.Sed ut perspiciatis doloremque laudantium.Sit voluptatem accusantium doloremque laudantium</p>
<div class="abs hero-btn narrow">VIEW COLLECTION</div>
<div class="abs slide-arrow" style="left:14px"><svg width="10" height="12" viewBox="0 0 10 12"><path d="M7 1L2 6l5 5" fill="none" stroke="#333" stroke-width="2.4"/></svg></div>
<div class="abs slide-arrow" style="left:880px"><svg width="10" height="12" viewBox="0 0 10 12"><path d="M3 1l5 5-5 5" fill="none" stroke="#333" stroke-width="2.4"/></svg></div>

<article class="abs category" style="left:137px">
  <div class="category-head">Necklaces</div>
  <div class="category-photo" role="img" aria-label="Diamond necklace on black" style="background:radial-gradient(ellipse at 50% 40%,#6c6c6c 0%,#1a1a1a 45%,#000 70%)"></div>
  <div class="abs view-more narrow">View More &gt;&gt;</div>
</article>
<article class="abs category" style="left:367px">
  <div class="category-head">Earrings</div>
  <div class="category-photo" role="img" aria-label="Ruby and diamond drop earring on white" style="background:radial-gradient(circle at 50% 62%,#b32a10 0%,#c7503a 18%,#e8e8e8 30%,#fff 45%)"></div>
  <div class="abs view-more narrow">View More &gt;&gt;</div>
</article>
<article class="abs category" style="left:598px">
  <div class="category-head">Bracelets</div>
  <div class="category-photo" role="img" aria-label="Diamond halo pendant on black" style="background:radial-gradient(circle at 48% 55%,#e6e8ec 0%,#9a9ea8 25%,#111 50%,#000 70%)"></div>
  <div class="abs view-more narrow">View More &gt;&gt;</div>
</article>

<form class="abs enquiry">
  <div class="abs ring-icon" role="img" aria-label="Solitaire engagement ring"></div>
  <h2>Engagement Ring</h2>
  <div class="abs field" style="top:49px">Name</div>
  <div class="abs field" style="top:81px">Email</div>
  <div class="abs field" style="top:113px">Phone</div>
  <div class="abs field" style="top:145px">Competitor Link</div>
  <div class="abs field" style="top:177px">Budget</div>
  <div class="abs submit narrow">SUBMIT</div>
</form>

<aside class="abs offer">
  <div class="abs offer-photo" role="img" aria-label="Diamond solitaire ring"></div>
  <b class="abs narrow">Special Offer</b>
  <span class="abs narrow">Click Here &gt;&gt;</span>
</aside>

<h2 class="abs products-title narrow">Our Products</h2>
<div class="abs pager" style="left:774px"><svg width="5" height="6" viewBox="0 0 5 6"><path d="M4 0L0 3l4 3z" fill="#fff"/></svg></div>
<div class="abs pager" style="left:790px"><svg width="5" height="6" viewBox="0 0 5 6"><path d="M1 0l4 3-4 3z" fill="#fff"/></svg></div>

<article class="abs product" style="left:362px;top:746px">
  <div class="abs product-photo" role="img" aria-label="Emerald cut diamond ring"></div>
  <h3>Diamond Rings</h3>
  <p>Nunc varius facilisis eros. Sed erat. In in velit quis arcu ornare laoreet. Nunc varius facilisis eros. Sed erat. Nunc varius</p>
  <div class="abs details narrow">Details</div>
</article>
<article class="abs product" style="left:590px;top:746px">
  <div class="abs product-photo" role="img" aria-label="Pavé diamond solitaire ring"></div>
  <h3>Diamond Rings</h3>
  <p>Nunc varius facilisis eros. Sed erat. In in velit quis arcu ornare laoreet. Nunc varius facilisis eros. Sed erat. Nunc varius</p>
  <div class="abs details narrow">Details</div>
</article>
<article class="abs product" style="left:362px;top:910px">
  <div class="abs product-photo" role="img" aria-label="Pear shaped diamond bezel ring"></div>
  <h3>Diamond Rings</h3>
  <p>Nunc varius facilisis eros. Sed erat. In in velit quis arcu ornare laoreet. Nunc varius facilisis eros. Sed erat. Nunc varius</p>
  <div class="abs details narrow">Details</div>
</article>
<article class="abs product" style="left:590px;top:910px">
  <div class="abs product-photo" role="img" aria-label="Princess cut diamond ring with pavé band"></div>
  <h3>Diamond Rings</h3>
  <p>Nunc varius facilisis eros. Sed erat. In in velit quis arcu ornare laoreet. Nunc varius facilisis eros. Sed erat. Nunc varius</p>
  <div class="abs details narrow">Details</div>
</article>

<footer class="abs site-footer"></footer>
<div class="abs footer-lines">
  Exquisite craftsmanship Finest quality diamonds<br>
  Will beat any competitors price by twenty to seventy percent guaranteed<br>
  Price quotes within 24 hours
</div>
<span class="abs social" style="left:730px;background:#3b5998" aria-label="Social link"></span>
<span class="abs social" style="left:752px;background:#3ea8dc" aria-label="Social link"></span>
<span class="abs social" style="left:773px;background:#f08a1c" aria-label="Social link"></span>
<span class="abs social" style="left:793px;background:#1a6fa8" aria-label="Social link"></span>
<p class="abs copyright">© 2013 velvetfacetgems.com, All Rights Reserved</p>

</body>
</html>
```